Business software developers new website

We need to redesign our website. Our current website is http://www.plumvista.net/index.html, which is outdated and needs a new look. We moved out from web design and have concentrated more on the back end of the systems, for example, system support and security and cloud-based applications. Our major clients include both private and government sectors. We would like to see some designs that are all in one page, simple and clean. Prefer illustrator or obstructed images instead of real-life photos. Must look futuristic yet friendly. Attached the new logo for your references and good luck.

Target Market(s)

Medium to big company for their IT or data management. Either improve or upgrade their current system.

Industry/Entity Type

Business Software

Number of Pages Required

1 page

Colors

Designer to choose colors to be used in the design.

Requirements
Must have
• Simple and clean. Individual assets must be provided in the correct size and format(png or jpeg). Prefer Goggle fonts. Even though the logo color is red, grey and black, still prefer some modern colors that go well with red. When design, must consider the possibility to convert it into responsive.
Nice to have
• White background
Should not have
• real life photos, no slider

```html
<!DOCTYPE html>
<html lang="en">
<head>
<meta charset="utf-8">
<title>Plumvista.net — Simplyfying the way you work</title>
<link rel="stylesheet" href="https://fonts.googleapis.com/css2?family=Ubuntu:wght@400;500;700&family=Arimo:wght@400;700&display=swap">
<style>
:root{
  --red:#f40d0d;
  --red-soft:#f9c6c9;
  --pink:#fde4e6;
  --pink-light:#fdf3f4;
  --pink-mid:#fde8ea;
  --ink:#111;
  --grey:#555;
  --grey-mid:#777;
  --placeholder:#f47c80;
  --white:#fff;
}
*{margin:0;padding:0;box-sizing:border-box}
html,body{width:796px;height:1200px;overflow:hidden;background:var(--white)}
.page{position:relative;width:796px;height:1200px;overflow:hidden;border-left:1px solid var(--red);border-right:1px solid var(--red);font-family:'Arimo',Arial,sans-serif;color:var(--grey)}
.backdrop{position:absolute;inset:0;z-index:0}
.page > *:not(.backdrop){position:absolute;z-index:1}
.top-bar{left:0;top:0;width:796px;height:6px;background:var(--red)}
.brand{left:77px;top:20px;font-family:'Ubuntu',sans-serif;font-size:31px;font-weight:400;color:#222;letter-spacing:-.5px;line-height:34px}
.tagline{left:77px;top:55px;font-family:'Arimo',sans-serif;font-weight:700;font-size:11px;color:#555;letter-spacing:-.1px}
.nav{left:404px;top:34px;display:flex;gap:0;font-family:'Arimo',sans-serif;font-weight:700;font-size:11px;color:#666}
.nav a{color:inherit;text-decoration:none;position:absolute;white-space:nowrap}
.nav .current{color:var(--red)}
.nav-underline{left:404px;top:58px;width:46px;height:2px;background:var(--red)}
.header-rule{left:0;top:83px;width:796px;height:1px;background:var(--red);opacity:.6}
.heading{font-family:'Ubuntu',sans-serif;font-weight:500;font-size:16.5px;color:var(--ink);text-align:center;white-space:nowrap;transform:translateX(-50%)}
.heading span{color:var(--red)}
.heading::after{content:"";display:block;margin:6px auto 0;width:64px;height:2px;background:var(--red)}
.copy{font-size:9.6px;line-height:14.1px;text-align:center;color:var(--grey)}
.col-divider{left:397px;top:130px;width:2px;height:99px;background:var(--red)}
.company-copy{left:18px;top:329px;width:760px;font-weight:700;font-size:9.3px;line-height:14.15px;text-align:center;color:#555}
.company-copy b{color:var(--red)}
.contact-card{left:122px;top:488px;width:203px;height:270px;border:1px solid var(--red);background:rgba(255,255,255,.15)}
.contact-card .card-head{height:44px;background:var(--red-soft);display:flex;align-items:center;justify-content:center;font-family:'Ubuntu',sans-serif;font-weight:500;font-size:16.5px;color:var(--ink)}
.contact-card .card-head span{color:var(--red);margin-left:4px}
.label{font-family:'Ubuntu',sans-serif;font-weight:500;font-size:11.5px;color:var(--ink)}
.value{font-family:'Ubuntu',sans-serif;font-size:11px;color:var(--red)}
.card-rule{left:179px;top:632px;width:92px;height:1px;background:var(--ink)}
.faq-item{left:421px;font-family:'Ubuntu',sans-serif;font-size:11px;color:#555;display:flex;align-items:center;gap:8px;white-space:nowrap}
.affiliate{left:490px;top:650px;width:217px;height:64px;display:flex;align-items:center;justify-content:center;gap:8px;font-family:'Ubuntu',sans-serif;font-weight:700;font-size:24px;color:var(--red);letter-spacing:1px}
.affiliate i{display:block;width:14px;height:14px;background:var(--red)}
.section-rule{left:0;top:786px;width:796px;height:1px;background:var(--red);opacity:.5}
.philosophy{left:30px;top:888px;width:250px;font-family:'Ubuntu',sans-serif;font-weight:500;font-size:11.7px;line-height:18.3px;text-align:center;color:var(--grey-mid);letter-spacing:-.2px}
.field{border:1px solid var(--red);background:var(--white);font-family:'Ubuntu',sans-serif;font-size:11px;color:var(--placeholder);padding-left:21px}
.send{left:483px;top:1089px;width:115px;height:38px;background:var(--red);color:var(--white);font-family:'Ubuntu',sans-serif;font-weight:500;font-size:11.5px;display:flex;align-items:center;justify-content:center}
.footer{left:0;top:1151px;width:796px;height:49px;background:var(--red);color:var(--white);font-family:'Ubuntu',sans-serif;font-weight:500;font-size:11.5px}
.footer .copyright{position:absolute;left:59px;top:17px}
.footer .sep{position:absolute;left:164px;top:11px;width:1px;height:24px;background:var(--white)}
.footer .site{position:absolute;left:175px;top:17px}
.footer .social{position:absolute;left:686px;top:13px;width:20px;height:20px;border-radius:50%;background:#3b5a9a}
</style>
</head>
<body>
<div class="page">
  <svg class="backdrop" width="796" height="1200" viewBox="0 0 796 1200" aria-hidden="true">
    <rect x="0" y="263" width="796" height="184" fill="#fdf3f4"/>
    <polygon points="796,109 796,263 500,263" fill="#fde4e6"/>
    <polygon points="500,263 796,263 796,447 145,447" fill="#fde4e6"/>
    <rect x="0" y="445" width="796" height="2" fill="#f9d2d5"/>
    <rect x="0" y="447" width="796" height="339" fill="#fde8ea"/>
    <polygon points="751,447 796,447 796,670 558,786 180,786" fill="#fff"/>
    <polygon points="0,786 180,786 0,900" fill="#fde8ea"/>
    <polygon points="560,786 796,786 796,860 0,1300 0,1110" fill="#fde8ea" opacity=".85"/>
    <polygon points="796,940 796,1151 460,1151" fill="#fde8ea"/>
  </svg>

  <div class="top-bar"></div>

  <div class="brand">plumvista.net</div>
  <div class="tagline">SIMPLYFYING THE WAY YOU WORK</div>

  <nav class="nav">
    <a class="current" style="left:6px">HOME</a>
    <a style="left:70px">OUR SERVICE</a>
    <a style="left:175px">OUR CLIENTS</a>
    <a style="left:280px">CONTACT</a>
  </nav>
  <div class="nav-underline"></div>
  <div class="header-rule"></div>

  <h2 class="heading" style="left:207px;top:120px">ABOUT <span>US</span></h2>
  <p class="copy" style="left:17px;top:160px;width:380px">We have provided web design, graphic design and application<br>development solutions for a wide variety of industries. We are known for<br>the quality of our work, affordable rates and our individual approach<br>to each customer. Our company offers a widevariety of professional web solution<br>and all this at very competitive prices!</p>
  <div class="col-divider"></div>
  <h2 class="heading" style="left:572px;top:120px">OUR <span>CLIENTS</span></h2>
  <p class="copy" style="left:400px;top:160px;width:360px">We undertake many projects from small businesses to<br>large corporations. We are also extremely experienced in the<br>long term support of comprehensive web based business systems providing<br>first class development, maintenance, data entry services and<br>enhancements. Click here to see more details.</p>

  <h2 class="heading" style="left:398px;top:285px">OUR <span>COMPANY</span></h2>
  <p class="company-copy"><b>Plumvista.net</b> is an Australian based Software and Web Development Company that provides individual technology solutions and professional software for clients worldwide.Our work is based on quality sales, customer and technical support services.Being oriented towards innovative productivity in our work, we come up with essential tools for online business enhancing. Our programming specialists focus on delivering solutions for small start-ups as well as large organizations and companies. The team of purposeful and experienced professionals works hard to extract maximum performance from modern information technologies.Providing the best quality of service and excellence of support we established a global presence in the software market. Our clients come from all over the world.Click here for more information on the services we provide.</p>

  <section class="contact-card">
    <div class="card-head">QUICK <span>CONTACT</span></div>
  </section>
  <svg style="left:147px;top:569px" width="26" height="22" viewBox="0 0 26 22" aria-hidden="true">
    <path d="M3 2 L8 1 L10 6 L7 8 Q10 14 17 16 L19 13 L24 15 L23 20 Q12 22 5 13 Q1 7 3 2Z" fill="var(--red)"/>
  </svg>
  <div class="label" style="left:189px;top:547px">PHONE</div>
  <div class="value" style="left:182px;top:563px">+61 7 5550 1824</div>
  <div class="label" style="left:188px;top:588px">MOBILE</div>
  <div class="value" style="left:182px;top:602px">+61 0491 570 156</div>
  <div class="card-rule"></div>
  <svg style="left:148px;top:680px" width="24" height="19" viewBox="0 0 24 19" aria-hidden="true">
    <rect x="0" y="0" width="24" height="19" rx="2" fill="var(--red)"/>
    <path d="M1 3 L12 11 L23 3" stroke="#fff" stroke-width="2" fill="none"/>
  </svg>
  <div class="label" style="left:189px;top:649px">SALES</div>
  <div class="value" style="left:186px;top:667px">info@plumvista.net</div>
  <div class="label" style="left:189px;top:700px">SUPPORT</div>
  <div class="value" style="left:186px;top:717px">support@plumvista.net</div>

  <h2 class="heading" style="left:607px;top:474px">FA<span>Q</span></h2>
  <div class="faq-item" style="top:517px">
    <svg width="10" height="16" viewBox="0 0 10 16" aria-hidden="true"><path d="M2 1 L8 8 L2 15" stroke="var(--red)" stroke-width="3" fill="none"/></svg>
    How much does a web site powered by Plumvista.net cost?
  </div>
  <div class="faq-item" style="top:561px">
    <svg width="10" height="16" viewBox="0 0 10 16" aria-hidden="true"><path d="M2 1 L8 8 L2 15" stroke="var(--red)" stroke-width="3" fill="none"/></svg>
    How much long does it take to have a web site designed?
  </div>

  <h2 class="heading" style="left:607px;top:606px">AFFILI<span>ATES</span></h2>
  <div class="affiliate"><i></i>KESTREL STUDIO</div>

  <div class="section-rule"></div>

  <h2 class="heading" style="left:166px;top:815px">PHILOS<span>OPHY</span></h2>
  <p class="philosophy">As web developers, we understand that a powerful and functional web site is a vital component of modern day marketing for companies of today. This is why our web site development team work with all of our clients to ensure their web site design will deliver to their target market.</p>

  <h2 class="heading" style="left:518px;top:815px">QUICK <span>CONTACT</span></h2>
  <div class="field" style="left:343px;top:873px;width:181px;height:35px;line-height:33px">What is your name?</div>
  <div class="field" style="left:558px;top:873px;width:181px;height:35px;line-height:33px">Where I can reply?</div>
  <div class="field" style="left:342px;top:920px;width:397px;height:148px;padding-top:16px">Talk to me.....</div>
  <div class="send">SEND MESSAGE</div>

  <footer class="footer">
    <span class="copyright">© Copyright 2011</span>
    <span class="sep"></span>
    <span class="site">Plumvista.net</span>
    <span class="social"></span>
  </footer>
</div>
</body>
</html>
```